Flyer für Kassensysteme
Zielgruppe
Kassensysteme - für diesen Flyer ist die Zielgruppe - Vereine - Unternehmen welche Vereinsfeste / Straßenfeste / Karnevalsitzungen oder Hausmessen bz. Messeverkäufe durchführen
Aufgabenstellung
optimal wäre DIN A5 einseitig welches auch so als Werbemail versendet werden kann. (unsere Internetpräsenz soll für diesen Firmenzweig von uns dann identisch angepasst werden) also ein schnell zu erfassender Flyer das es um Leih und Mietkassen für oben genannte Aktivitäten geht. kleiner Preis große Ersparnis Transparenz einfach zu bedienen

```html
<!DOCTYPE html>
<html lang="de">
<head>
<meta charset="utf-8">
<title>Leih- / Mietkassen Flyer</title>
<link href="https://fonts.googleapis.com/css2?family=Montserrat:wght@400;500;600;700;800&display=swap" rel="stylesheet">
<style>
  :root{
    --purple:#6b2a6e;
    --navy:#3e5672;
    --navy-photo:#2f4866;
    --sky:#a9cfe6;
    --sky-photo:#8fb6d3;
    --text:#444a52;
    --white:#ffffff;
    --page:#e6e7e9;
  }
  *{margin:0;padding:0;box-sizing:border-box}
  html,body{width:1200px;height:1200px;overflow:hidden;background:var(--page);font-family:"Montserrat",sans-serif}
  .flyer{position:absolute;left:254px;top:108px;width:692px;height:981px;background:var(--white);overflow:hidden}
  .hero{position:absolute;left:0;top:0;width:692px;height:355px}
  .brand{position:absolute;left:250px;top:58px;width:200px;display:flex;align-items:center;justify-content:center;gap:8px;color:var(--navy);font-weight:700;font-size:24px;letter-spacing:1px}
  .brand-mark{width:18px;height:18px;background:var(--sky)}
  .product{position:absolute;left:67px;top:190px;width:554px;height:322px;border-radius:14px;background:linear-gradient(160deg,#5b6068 0%,#2d3036 55%,#8b9097 100%)}
  .headline{position:absolute;left:0;top:545px;width:692px;text-align:center;color:var(--purple);font-weight:800;font-size:52px;letter-spacing:.5px}
  .question{position:absolute;left:0;top:608px;width:692px;text-align:center;color:var(--text);font-weight:700;font-size:20px;line-height:31px}
  .body-copy{position:absolute;left:0;top:696px;width:692px;text-align:center;color:var(--text);font-weight:500;font-size:14.5px;line-height:21px}
  .club-offer{position:absolute;left:44px;top:795px;width:605px;height:45px;background:var(--purple);border-radius:10px 10px 0 0;color:var(--white);font-weight:700;font-size:16px;display:flex;align-items:center;justify-content:center}
  .contact{position:absolute;left:0;top:836px;width:692px;height:145px}
  .more-info{position:absolute;left:42px;top:860px;color:var(--navy);font-weight:800;font-size:34px;line-height:44px}
  .phone-icon{position:absolute;left:237px;top:862px}
  .phone{position:absolute;left:298px;top:864px;color:var(--white);font-weight:700;font-size:32px;line-height:40px}
  .web{position:absolute;left:236px;top:922px;color:var(--sky);font-weight:700;font-size:16px}
</style>
</head>
<body>
<div class="flyer">
  <svg class="hero" viewBox="0 0 692 355" width="692" height="355">
    <rect x="0" y="0" width="692" height="344" fill="var(--sky-photo)" role="img" aria-label="Foto: Besucherin an einem Marktstand auf einem Fest"/>
    <polygon points="508,0 692,0 692,344 417,344" fill="var(--navy-photo)" role="img" aria-label="Foto: Bratwürste auf einem Grill"/>
    <polygon points="235,0 508,0 457,152 184,152" fill="var(--white)"/>
    <rect x="0" y="344" width="692" height="11" fill="var(--sky)"/>
  </svg>
  <div class="brand"><span class="brand-mark"></span>KASSENWERK</div>
  <div class="product" role="img" aria-label="Produktfoto: Touchscreen-Kassensystem mit Tastatur und Bondrucker"></div>

  <h1 class="headline">LEIH- / MIETKASSEN</h1>
  <p class="question">Sie planen bzw. veranstalten ein Vereinsfest eine<br>Hausmesse oder einen Sonderverkauf?</p>
  <p class="body-copy">Sparen Sie Zeit und Nerven mit der transparenten Abrechnung<br>über eine unserer Mietkassen - kinderleicht zu bedienen<br>und mit allen Funktionen eines modernen Kassensystems ausgestattet.</p>
  <div class="club-offer">Für Vereine bieten wir unsere Leihkassen mit einer Miet-TSE an.</div>

  <svg class="contact" viewBox="0 0 692 145" width="692" height="145">
    <rect x="0" y="0" width="692" height="6" fill="var(--sky)"/>
    <rect x="0" y="8" width="692" height="137" fill="var(--sky)"/>
    <polygon points="209,8 692,8 692,145 163,145" fill="var(--navy)"/>
  </svg>
  <div class="more-info">MORE<br>INFO</div>
  <svg class="phone-icon" width="44" height="44" viewBox="0 0 44 44">
    <circle cx="22" cy="22" r="22" fill="var(--sky)"/>
    <path d="M15 12c1-1 2.5-1 3.3.1l2.4 3.3c.6.9.5 2-.3 2.7l-1.5 1.3c1 2.4 2.9 4.3 5.3 5.4l1.4-1.5c.7-.8 1.9-.9 2.7-.3l3.3 2.4c1.1.8 1.1 2.3.1 3.3l-1.6 1.6c-1.2 1.2-3 1.5-4.5.8-5.4-2.3-9.6-6.5-11.9-11.9-.6-1.5-.3-3.3.9-4.5z" fill="var(--navy)"/>
  </svg>
  <div class="phone">[0000] 55123-0</div>
  <div class="web">https://www.kassenwerk-beispiel.de/leih-mietkassen/</div>
</div>
</body>
</html>
```